Webpage Wordpress Redesign

Need a redesign of a current wordpress. Project did not meet needed requirements and formatting was never completed. Functionality is fairly close to where it should be but need some help to make it usable.

Current site - http://brightmarsh.org

As you can see images are not visible any longer for some reason. Needs to have a clean simple layout with the ability to receive donations through paypal.

Requirements
Must have
• Needs to be able to have picture functionality. Needs to have a usable email sign-up collection option, even if that means using the form created through mailchimp or something. Need to have a blog like page for easy update of new articles and information. Needs to have a clean simple layout with the ability to receive donations through paypal.

```html
<!DOCTYPE html>
<html lang="en">
<head>
<meta charset="utf-8">
<title>Brightmarsh Life Alliance</title>
<link href="https://fonts.googleapis.com/css2?family=Open+Sans:ital,wght@0,300;0,400;0,600;0,700;0,800;1,400;1,700&family=Roboto+Slab:wght@400;700&display=swap" rel="stylesheet">
<style>
:root{
  --magenta:#c4197c;
  --cyan:#2bb5d8;
  --ink:#2b2b2b;
  --body:#555555;
  --muted:#777777;
  --band:#f3f3f3;
  --footer:#ececec;
  --bar:#cacaca;
  --line:#3a3a3a;
}
*{box-sizing:border-box;margin:0;padding:0}
html,body{width:1200px;height:2247px;overflow:hidden;background:#fff}
body{font-family:"Open Sans",Arial,sans-serif;color:var(--body);position:relative}
.wrap{width:900px;margin-left:150px;position:relative}

/* header */
.site-header{height:132px;position:relative}
.brand{position:absolute;left:150px;top:12px;display:flex;align-items:center;gap:12px}
.brand-dot{width:60px;height:60px;border-radius:50%;background:var(--cyan)}
.brand-name{font-family:"Open Sans",Arial,sans-serif;font-weight:800;font-size:17px;color:var(--magenta);line-height:1.15;width:130px}
.header-social{position:absolute;right:150px;top:28px;display:flex;gap:9px}
.header-social span{width:14px;height:14px;background:#c9c9c9;display:block}
.main-nav{position:absolute;right:150px;top:61px;display:flex;align-items:center}
.main-nav a{font-weight:700;font-size:18px;color:var(--ink);text-decoration:none;margin-left:36px;letter-spacing:.2px}
.main-nav .nav-donate{background:var(--magenta);color:#fff;border-radius:4px;padding:7px 16px;margin-left:44px;font-size:17px}

.hero{height:434px;background:linear-gradient(180deg,#cfcbc3 0%,#9e948c 40%,#6d5d58 75%,#8a7d74 100%)}

/* news */
.news{padding-top:88px}
.section-title{display:flex;align-items:center;justify-content:center;gap:12px;font-family:"Roboto Slab",Georgia,serif;font-weight:700;font-size:25px;color:var(--cyan);letter-spacing:.3px}
.section-title::before,.section-title::after{content:"";width:112px;height:2px;background:var(--cyan)}
.news-grid{display:grid;grid-template-columns:repeat(4,198px);column-gap:36px;row-gap:78px;margin-top:27px}
.news-card .thumb{height:140px}
.news-card h3{font-weight:700;font-size:16.5px;line-height:22px;color:var(--ink);margin-top:24px}
.news-card p{font-weight:300;font-size:14.5px;line-height:22.5px;color:var(--body);margin-top:10px;height:90px;overflow:hidden}
.read-more{display:block;text-align:right;font-style:italic;font-weight:700;font-size:11px;color:var(--cyan);text-decoration:none;margin-top:12px}

/* call to action */
.cta{position:absolute;left:0;top:1562px;width:1200px;height:221px;background:var(--band);text-align:center}
.cta::before{content:"";position:absolute;left:587px;top:0;border-left:13px solid transparent;border-right:13px solid transparent;border-top:13px solid #fff}
.cta h2{font-family:"Roboto Slab",Georgia,serif;font-weight:700;font-size:26px;color:var(--magenta);margin-top:52px;letter-spacing:.3px}
.cta p{font-size:18px;font-weight:300;color:var(--body);margin-top:2px}
.cta .btn-donate{display:inline-block;margin-top:17px;width:225px;height:56px;line-height:56px;background:var(--magenta);color:#fff;border-radius:6px;font-weight:700;font-size:18px;text-decoration:none}

/* footer */
.site-footer{position:absolute;left:0;top:1783px;width:1200px;height:414px;background:var(--footer)}
.footer-cols{display:grid;grid-template-columns:repeat(3,276px);column-gap:36px;margin-top:69px}
.footer-col h4{font-family:"Roboto Slab",Georgia,serif;font-weight:700;font-size:14px;color:var(--ink);padding-bottom:8px;border-bottom:2px solid var(--line);letter-spacing:.2px}
.field{display:block;height:36px;background:#fff;margin-top:10px;padding:0 12px;line-height:36px;font-style:italic;font-size:14px;color:#555}
.footer-col .field:first-of-type{margin-top:21px}
.btn-signup{display:block;width:150px;height:37px;margin-top:12px;background:var(--cyan);color:#fff;border-radius:5px;text-align:center;line-height:37px;font-weight:700;font-size:15px}
.community{margin-top:21px;background:#fff;height:224px;padding:10px 10px 0}
.community-head{display:flex;gap:8px;padding-bottom:10px;border-bottom:1px solid #e3e3e3}
.community-avatar{width:46px;height:46px;border-radius:50%;background:var(--cyan)}
.community-name{font-weight:700;font-size:12.5px;color:#3b5998}
.like-btn{display:inline-block;margin-top:4px;background:#5b74a8;color:#fff;font-size:10px;font-weight:700;padding:2px 7px;border-radius:2px}
.community-count{font-size:10px;color:#333;margin-top:8px}
.community-count b{color:#3b5998;font-weight:400}
.faces{display:grid;grid-template-columns:repeat(5,46px);gap:6px;margin-top:10px}
.faces span{height:46px;display:block}
.community-foot{font-size:9px;color:#555;border-top:1px solid #e3e3e3;margin-top:10px;padding-top:6px}
.contact-list{list-style:none;margin-top:21px}
.contact-list li{display:flex;align-items:center;gap:10px;font-size:14.5px;color:#444;height:24px}
.contact-list svg{width:14px;height:14px;flex:none;fill:#444}
.footer-social{display:flex;gap:12px;margin-top:18px}
.footer-social span{width:14px;height:14px;background:#555;display:block}

.bottom-bar{position:absolute;left:0;top:2197px;width:1200px;height:50px;background:var(--bar)}
.bottom-bar .copy{position:absolute;left:150px;top:17px;font-family:"Roboto Slab",Georgia,serif;font-size:12px;color:#333}
.bottom-nav{position:absolute;right:150px;top:16px;font-weight:700;font-size:11.5px;color:#333}
.bottom-nav a{color:#333;text-decoration:none}
.to-top{position:absolute;left:1129px;top:2184px;width:42px;height:42px;border-radius:50%;background:#7a7a7a}
.to-top svg{position:absolute;left:13px;top:13px}
</style>
</head>
<body>

<header class="site-header">
  <div class="brand"><span class="brand-dot"></span><span class="brand-name">Brightmarsh Life Alliance</span></div>
  <div class="header-social" aria-label="Social links"><span></span><span></span><span></span></div>
  <nav class="main-nav">
    <a href="#">HOME</a><a href="#">ABOUT US</a><a href="#">NEWS</a><a href="#">CONTACT US</a><a href="#" class="nav-donate">DONATE</a>
  </nav>
</header>

<div class="hero" role="img" aria-label="Group photo of supporters on the steps of the state capitol"></div>

<section class="news wrap">
  <h2 class="section-title">RECENT NEWS</h2>
  <div class="news-grid">
    <article class="news-card">
      <div class="thumb" role="img" aria-label="Officials at a press event" style="background:linear-gradient(135deg,#c9b79a,#3b302c 60%,#1d1a1a)"></div>
      <h3>Judge Rules Morning After Pill Legal for Minors</h3>
      <p>As a pro-life organization we are extremely disappointed by the ruling sent down from U.S. District Judge Edward Hale. A judge has now forced</p>
      <a class="read-more" href="#">READ MORE &gt;</a>
    </article>
    <article class="news-card">
      <div class="thumb" role="img" aria-label="Speaker at a podium in a hearing room" style="background:linear-gradient(135deg,#6b5240,#4a3528 60%,#2e221c)"></div>
      <h3>Protect the Infants Born Alive Bill!</h3>
      <p>Don't let Family Choice Clinics get away with ending the lives of babies born from botched abortions. Support this most important pro-life law by</p>
      <a class="read-more" href="#">READ MORE &gt;</a>
    </article>
    <article class="news-card">
      <div class="thumb" role="img" aria-label="Close-up of a baby in a blue hat" style="background:linear-gradient(160deg,#1f8fa3,#44b3c4 45%,#e2b9a4 75%)"></div>
      <h3>One Abortion Every 94 Seconds in the United States</h3>
      <p>Family Choice Clinics continues to be the single largest abortion provider in the United States. And regardless of what they say their data and their</p>
      <a class="read-more" href="#">READ MORE &gt;</a>
    </article>
    <article class="news-card">
      <div class="thumb" role="img" aria-label="Historic capitol building under blue sky" style="background:linear-gradient(180deg,#6f93c8,#a9bfdc 55%,#e3e3df 70%,#4d6a3e)"></div>
      <h3>April 18: Celebrate Life Day</h3>
      <p>Come Join Us April 18, 2013 to attend the 5th annual “Celebrate Life Day” at the State Capitol Building with Brightmarsh Life Alliance. Events of</p>
      <a class="read-more" href="#">READ MORE &gt;</a>
    </article>
    <article class="news-card">
      <div class="thumb" role="img" aria-label="Grandfather holding a baby" style="background:linear-gradient(135deg,#5a3a30,#9a6b5a 50%,#e4c7c0)"></div>
      <h3>About Brightmarsh Life Alliance</h3>
      <p>Brightmarsh Life Alliance is a nonprofit, nonpartisan, grass-roots public service organization dedicated to protecting and fostering the</p>
      <a class="read-more" href="#">READ MORE &gt;</a>
    </article>
    <article class="news-card">
      <div class="thumb" role="img" aria-label="Small bird held in hands" style="background:linear-gradient(135deg,#8d8580,#5c534e 55%,#c9c2bc)"></div>
      <h3>Lorem Ipsum Dolor Sit Amet Conse</h3>
      <p>Morbi ullamcorper purus quis erat aliquet faucibus gravida nunc posuere. Suspendisse at mauris et ante rutrum pellentesque sit amet quis mi.</p>
      <a class="read-more" href="#">READ MORE &gt;</a>
    </article>
    <article class="news-card">
      <div class="thumb" role="img" aria-label="Child hugging a husky dog" style="background:linear-gradient(135deg,#2c2b2b,#8c8a88 50%,#3f9aa8)"></div>
      <h3>Cultrices Risu Vestibulum Massa Elit Putrum</h3>
      <p>Curabitur fermentum lectus id justo euismod dignissim. Aenean ac nunc erat. Nulla eros enim, commodo in tempor iaculis, venenatis</p>
      <a class="read-more" href="#">READ MORE &gt;</a>
    </article>
    <article class="news-card">
      <div class="thumb" role="img" aria-label="Family walking in a sunny field" style="background:linear-gradient(180deg,#7fb0d8,#c7dbe8 45%,#9a9a4e 70%,#6f7a3a)"></div>
      <h3>Semper Aliquam Class Daptent Taciti Ociosqu</h3>
      <p>Ut leo diam, hendrerit eget hendrerit tincidunt, fermentum id neque. Phasellus malesuada diam non ornare accumsan. Morbi vitae ultrices lectus, at</p>
      <a class="read-more" href="#">READ MORE &gt;</a>
    </article>
  </div>
</section>

<section class="cta">
  <h2>LIFE: BECASEU EVERY LIFE IS WORTH LIVING</h2>
  <p>Brightmarsh Life Alliance defends innocent human life from conception until natural death.</p>
  <a class="btn-donate" href="#">DONATE NOW!</a>
</section>

<footer class="site-footer">
  <div class="wrap footer-cols">
    <div class="footer-col">
      <h4>NEWSLETTER SIGNUP</h4>
      <span class="field">Name</span>
      <span class="field">Email</span>
      <span class="btn-signup">SIGN ME UP!</span>
    </div>
    <div class="footer-col">
      <h4>JOIN OUR COMMUNITY</h4>
      <div class="community">
        <div class="community-head">
          <span class="community-avatar"></span>
          <div><div class="community-name">Brightmarsh Life Alliance, Inc.</div><span class="like-btn">Like</span></div>
        </div>
        <div class="community-count">1,664 people like <b>Brightmarsh Life Alliance, Inc.</b></div>
        <div class="faces" role="img" aria-label="Profile pictures of community members">
          <span style="background:#7b6a5a"></span><span style="background:#a58a6e"></span><span style="background:#8c7a60"></span><span style="background:#6e5a4a"></span><span style="background:#b59a7a"></span>
          <span style="background:#9aa0a8"></span><span style="background:#b7a090"></span><span style="background:#4a4040"></span><span style="background:#a07aa0"></span><span style="background:#8a5a6a"></span>
        </div>
        <div class="community-foot">Social plugin</div>
      </div>
    </div>
    <div class="footer-col">
      <h4>GET IN TOUCH</h4>
      <ul class="contact-list">
        <li><svg viewBox="0 0 16 16"><path d="M3 1l3 3-2 2c1 2 3 4 5 5l2-2 3 3-2 3C7 15 1 9 0 3z"/></svg>555-010-LIFE</li>
        <li><svg viewBox="0 0 16 16"><path d="M0 3h16v10H0z M1 4l7 5 7-5" fill="none" stroke="#444" stroke-width="1.6"/></svg>hello@brightmarsh.org</li>
        <li><svg viewBox="0 0 16 16"><path d="M8 1l8 7h-2v7h-4v-5H6v5H2V8H0z"/></svg>Marsh Harbor, Florida</li>
        <li><svg viewBox="0 0 16 16"><path d="M0 2h16v12H0z M2 5h5v6H2z M9 5h5v1.5H9z M9 8h5v1.5H9z" fill-rule="evenodd"/></svg>Dana Whitlow, Executive Director</li>
      </ul>
      <div class="footer-social" aria-label="Social links"><span></span><span></span><span></span></div>
    </div>
  </div>
</footer>

<div class="bottom-bar">
  <span class="copy">©2013 Brightmarsh Life Alliance, Inc.</span>
  <nav class="bottom-nav"><a href="#">HOME</a> / <a href="#">ABOUT US</a> / <a href="#">NEWS</a> / <a href="#">CONTACT US</a> / <a href="#">DONATE</a></nav>
</div>
<a class="to-top" href="#" aria-label="Back to top"><svg width="16" height="16" viewBox="0 0 16 16"><path d="M2 11l6-6 6 6" fill="none" stroke="#fff" stroke-width="2"/></svg></a>

</body>
</html>
```